tovrin company need business card, envelope and letterhead design

Check on the attached file wherein you can find our logo and information about the company
Business card will double sided English version and Arabic version

Industry/Entity Type

Business

Requirements
Must have
• include the design also for the letterhead and envelop
Nice to have

```html
<!DOCTYPE html>
<html lang="en">
<head>
<meta charset="utf-8">
<title>Tovrin — Business Card</title>
<link rel="stylesheet" href="https://fonts.googleapis.com/css2?family=PT+Sans:wght@400;700&display=swap">
<style>
  :root {
    --stage: #000000;
    --card-front: #f2f2f2;
    --brand-blue: #1a6fba;
    --back-blue: #1477c6;
    --back-blue-light: #2a8ad6;
    --ink: #2b2b2b;
    --white: #ffffff;
  }
  * { margin: 0; padding: 0; box-sizing: border-box; }
  html, body {
    width: 1200px; height: 900px; overflow: hidden;
    background: var(--stage);
    font-family: "PT Sans", Arial, sans-serif;
  }
  .canvas { position: relative; width: 1200px; height: 900px; }

  .card { position: absolute; top: 200px; width: 310px; height: 502px; }
  .card-front {
    left: 265px; background: var(--card-front);
    border-radius: 52px 0 52px 0;
  }
  .card-back {
    left: 641px; width: 309px;
    background: linear-gradient(160deg, var(--back-blue-light), var(--back-blue) 60%);
    border-radius: 0 52px 0 52px;
    display: flex; align-items: center; justify-content: center;
  }

  .brand { position: absolute; left: 27px; top: 124px; display: flex; align-items: center; gap: 10px; }
  .brand-mark { width: 26px; height: 26px; background: var(--brand-blue); }
  .brand-name {
    font-weight: 700; font-size: 34px; letter-spacing: 2px;
    color: var(--brand-blue); line-height: 1;
  }

  .contact { position: absolute; left: 27px; top: 292px; color: var(--ink); }
  .contact-name { font-weight: 700; font-size: 14px; color: var(--brand-blue); line-height: 18px; }
  .contact-role { font-size: 14px; line-height: 17px; margin-bottom: 7px; }
  .contact-list { list-style: none; }
  .contact-list li {
    display: flex; align-items: center; gap: 7px;
    font-size: 14px; line-height: 18px;
  }
  .contact-list svg { width: 11px; height: 11px; fill: var(--brand-blue); flex: none; }
  .contact-address { font-size: 14px; line-height: 18px; margin-top: 6px; }

  .back-brand { display: flex; align-items: center; gap: 12px; }
  .back-brand .brand-mark { background: var(--white); width: 30px; height: 30px; }
  .back-brand .brand-name { color: var(--white); font-size: 40px; }
</style>
</head>
<body>
<div class="canvas">
  <section class="card card-front">
    <div class="brand">
      <span class="brand-mark"></span>
      <span class="brand-name">TOVRIN</span>
    </div>

    <div class="contact">
      <p class="contact-name">FARIS BIN OMAR AL NADHEER</p>
      <p class="contact-role">General Manager</p>
      <ul class="contact-list">
        <li><svg viewBox="0 0 12 12"><path d="M3 0h6a1 1 0 0 1 1 1v10a1 1 0 0 1-1 1H3a1 1 0 0 1-1-1V1a1 1 0 0 1 1-1zm0.6 1.4v7.6h4.8V1.4zM6 9.8a0.8 0.8 0 1 0 0.01 0z"/></svg>+966 555 381 720</li>
        <li><svg viewBox="0 0 12 12"><path d="M0 4c0-2 12-2 12 0v1.2H9V3.8H3v1.4H0zM2 6h8l1.5 5H0.5zm4 1.2a1.6 1.6 0 1 0 0.01 0z"/></svg>011 4720336</li>
        <li><svg viewBox="0 0 12 12"><path d="M3 0h5l1 1v3H3zM1 4h10a1 1 0 0 1 1 1v6a1 1 0 0 1-1 1H1a1 1 0 0 1-1-1V5a1 1 0 0 1 1-1zm2 2v1.2h6V6zm0 2.3v1.2h6V8.3z"/></svg>011 4720 337</li>
        <li><svg viewBox="0 0 12 12"><path d="M0 2h12v8H0zm1 1l5 3.6L11 3v-.1H1z"/></svg>tovrin.sa@mailbox.com</li>
      </ul>
      <p class="contact-address">Qasr Al Noor Road, Al Waha,<br>P.O. Box 5214-11683<br>Kingdom of Saudi Arabia</p>
    </div>
  </section>

  <section class="card card-back">
    <div class="back-brand">
      <span class="brand-mark"></span>
      <span class="brand-name">TOVRIN</span>
    </div>
  </section>
</div>
</body>
</html>
```